We need a business card design for a new company based in Queensland, Australia using our new logo (attached) using similar or complimentary colours and showing a softness and honesty. On the back we would like space to write three appointment or session times.ie. Session 1.... Session 2... Session 3.

Industry/Entity Type

Business

Contact Information for Business Card

name, title, mobile, email, web, address, facebook,

Requirements
Must have
• on back of card must have following:
• For information about Tranquivant Therapy please visit www.thevalendrawork.com
• Please use the registered symbol of an R in a circle at end of Tranquivant Therapy please.

```html
<!DOCTYPE html>
<html lang="en">
<head>
<meta charset="utf-8">
<title>Quiet Harbour Wellness – Business Cards</title>
<link rel="stylesheet" href="https://fonts.googleapis.com/css2?family=Source+Sans+3:ital,wght@0,400;0,600;1,400&display=swap">
<style>
:root{
  --bg:#d9c6ae;
  --card:#fbfbfb;
  --blue:#1f56a8;
  --blue-dark:#1b4f9e;
  --blue-light:#2f8fd6;
  --green:#8dc63f;
  --green-dark:#3f6f16;
  --text:#555;
  --rule:#cfcfcf;
  --line:#3468b2;
}
*{margin:0;padding:0;box-sizing:border-box}
html,body{width:1200px;height:1070px;overflow:hidden}
body{background:var(--bg);font-family:"Source Sans 3",Arial,sans-serif;position:relative;color:var(--text)}
.card{position:absolute;width:493px;height:281px;background:var(--card);box-shadow:0 2px 6px rgba(0,0,0,.3);overflow:hidden}
.c1{left:85px;top:69px}.c2{left:618px;top:69px}
.c3{left:85px;top:410px}.c4{left:618px;top:410px}
.c5{left:85px;top:735px}.c6{left:618px;top:735px}

.brand{position:absolute;display:flex;align-items:center;justify-content:center;gap:7px;white-space:nowrap}
.brand-mark{flex:none;border-radius:50%;background:var(--green)}
.brand-name{color:var(--blue);font-weight:400;text-transform:uppercase;letter-spacing:-.2px}
.brand.lg{width:290px}
.brand.lg .brand-mark{width:11px;height:11px}
.brand.lg .brand-name{font-size:19px}
.brand.sm{width:200px}
.brand.sm .brand-mark{width:8px;height:8px}
.brand.sm .brand-name{font-size:14px}

.divider{position:absolute;left:290px;top:40px;width:1px;height:222px;background:var(--rule)}
.person{position:absolute;left:312px;top:40px}
.person .name{color:var(--blue);font-weight:600;font-size:19px;line-height:1.2}
.person .title{color:var(--green);font-size:14px;margin-top:1px}
.person .addr{font-size:12.5px;line-height:17px;margin-top:9px}
.contacts{list-style:none;margin-top:10px;font-size:12.5px;line-height:19px}
.contacts li{display:flex;align-items:center;gap:7px}
.contacts svg{width:13px;height:13px;fill:var(--blue)}

.band{position:absolute;left:0;bottom:0;width:100%;height:20px}
.band .blue{position:absolute;left:0;top:0;width:300px;height:20px;background:linear-gradient(90deg,var(--blue-dark),var(--blue-light) 55%,var(--blue-dark))}
.band .green{position:absolute;left:288px;right:0;top:0;height:20px;background:var(--green);clip-path:polygon(6px 0,100% 0,100% 100%,0 100%)}
.band .green::before{content:"";position:absolute;left:4px;top:0;width:3px;height:20px;background:#fff;transform:skewX(-18deg)}
.band .label{position:absolute;left:24px;right:0;top:0;line-height:20px;color:var(--green-dark);font-style:italic;font-size:12.5px;display:flex;align-items:center;gap:5px}
.band .spaced{letter-spacing:2.4px;left:14px;right:10px;justify-content:center}
.fb-square{width:12px;height:12px;background:var(--blue)}

.session{position:absolute;display:flex;align-items:flex-end;color:var(--blue);font-weight:600;font-size:14px}
.session .write{flex:1;border-bottom:1px solid var(--line);margin-left:8px;margin-bottom:4px}
.note{position:absolute;font-style:italic;color:var(--text);font-size:12.5px}
.info{position:absolute;font-style:italic;color:var(--text);font-size:12.5px;line-height:18px}
.info a,.footer-info a{color:var(--blue);font-weight:600;text-decoration:none}
.footer-info{position:absolute;font-size:13px;color:var(--text)}
.right{text-align:right}
</style>
</head>
<body>

<section class="card c1">
  <div class="brand lg" style="left:8px;top:152px">
    <span class="brand-mark"></span><span class="brand-name">Quiet Harbour Wellness</span>
  </div>
  <div class="divider"></div>
  <div class="person">
    <div class="name">Daniel Hartley</div>
    <div class="title">Director</div>
    <div class="addr">Suite 14 Marlow Lane<br>QLD 4217, Australia</div>
    <ul class="contacts">
      <li><svg viewBox="0 0 16 16"><path d="M1 6c0-3 14-3 14 0v2h-4V6H5v2H1zM3 9h10l1 6H2z"/></svg>07 5512 3480</li>
      <li><svg viewBox="0 0 16 16"><path d="M4 0h8v16H4zM5.5 2v10h5V2z"/></svg>0412 558 903</li>
      <li><svg viewBox="0 0 16 16"><path d="M4 0h8v5H4zM1 6h14v7H1zM4 11h8v5H4z"/></svg>0412 558 904</li>
      <li><svg viewBox="0 0 16 16"><path d="M0 3h16v10H0zM1 4l7 5 7-5z" fill-rule="evenodd"/></svg>info@quietharbour.net</li>
      <li><span class="fb-square"></span>quietharbourwellness</li>
    </ul>
  </div>
  <div class="band"><div class="blue"></div><div class="green"><div class="label spaced">www.quietharbour.net</div></div></div>
</section>

<section class="card c2">
  <div class="brand lg" style="left:8px;top:152px">
    <span class="brand-mark"></span><span class="brand-name">Quiet Harbour Wellness</span>
  </div>
  <div class="divider"></div>
  <div class="person">
    <div class="name">Daniel Hartley</div>
    <div class="title">Director</div>
    <div class="addr">Suite 14 Marlow Lane<br>QLD 4217, Australia</div>
    <ul class="contacts">
      <li><svg viewBox="0 0 16 16"><path d="M1 6c0-3 14-3 14 0v2h-4V6H5v2H1zM3 9h10l1 6H2z"/></svg>07 5512 3480</li>
      <li><svg viewBox="0 0 16 16"><path d="M4 0h8v16H4zM5.5 2v10h5V2z"/></svg>0412 558 903</li>
      <li><svg viewBox="0 0 16 16"><path d="M4 0h8v5H4zM1 6h14v7H1zM4 11h8v5H4z"/></svg>0412 558 904</li>
      <li><svg viewBox="0 0 16 16"><path d="M0 3h16v10H0zM1 4l7 5 7-5z" fill-rule="evenodd"/></svg>info@quietharbour.net</li>
      <li><svg viewBox="0 0 16 16"><circle cx="8" cy="8" r="7" fill="none" stroke="#1f56a8" stroke-width="1.3"/><path d="M1 8h14M8 1c-4 4-4 10 0 14M8 1c4 4 4 10 0 14" fill="none" stroke="#1f56a8" stroke-width="1.1"/></svg>www.quietharbour.net</li>
    </ul>
  </div>
  <div class="band"><div class="blue"></div><div class="green"><div class="label"><span class="fb-square"></span>quietharbourcare</div></div></div>
</section>

<section class="card c3">
  <div class="brand sm" style="left:280px;top:73px">
    <span class="brand-mark"></span><span class="brand-name">Quiet Harbour Wellness</span>
  </div>
  <div class="session" style="left:31px;top:122px;width:432px">Session 1:<span class="write"></span></div>
  <div class="session" style="left:31px;top:160px;width:432px">Session 2:<span class="write"></span></div>
  <div class="session" style="left:31px;top:197px;width:432px">Session 3:<span class="write"></span></div>
  <div class="note" style="left:0;width:493px;top:227px;text-align:center;font-size:11px">Please give 24 hours notice cancelling your appointment or a fee may be charged</div>
  <div class="footer-info" style="left:31px;top:249px">For more information about Tranquivant Therapy® see <a>www.thevalendrawork.com</a></div>
</section>

<section class="card c4">
  <div class="info" style="left:30px;top:51px">For more information about<br>Tranquivant Therapy® see<br><a>www.thevalendrawork.com</a></div>
  <div class="brand sm" style="left:278px;top:73px">
    <span class="brand-mark"></span><span class="brand-name">Quiet Harbour Wellness</span>
  </div>
  <div class="session" style="left:28px;top:138px;width:432px">Session 1:<span class="write"></span></div>
  <div class="session" style="left:28px;top:176px;width:432px">Session 2:<span class="write"></span></div>
  <div class="session" style="left:28px;top:213px;width:432px">Session 3:<span class="write"></span></div>
  <div class="note" style="left:36px;top:245px">Please give 24 hours notice cancelling your appointment or a fee may be charged</div>
</section>

<section class="card c5">
  <div class="brand sm" style="left:160px;top:70px">
    <span class="brand-mark"></span><span class="brand-name">Quiet Harbour Wellness</span>
  </div>
  <div class="session" style="left:28px;top:113px;width:432px">Session 1:<span class="write"></span></div>
  <div class="session" style="left:28px;top:151px;width:432px">Session 2:<span class="write"></span></div>
  <div class="session" style="left:28px;top:188px;width:432px">Session 3:<span class="write"></span></div>
  <div class="info" style="left:28px;top:219px;font-size:12.5px;line-height:16px">Please give 24 hours notice<br>cancelling your appointment<br>or a fee may be charged</div>
  <div class="info right" style="right:30px;top:219px;font-size:12.5px;line-height:16px">For more information about<br>Tranquivant Therapy® see<br><a>www.thevalendrawork.com</a></div>
</section>

<section class="card c6">
  <div class="brand sm" style="left:14px;top:73px">
    <span class="brand-mark"></span><span class="brand-name">Quiet Harbour Wellness</span>
  </div>
  <div class="info right" style="right:31px;top:51px">For more information about<br>Tranquivant Therapy® see<br><a>www.thevalendrawork.com</a></div>
  <div class="session" style="left:28px;top:138px;width:432px">Session 1:<span class="write"></span></div>
  <div class="session" style="left:28px;top:176px;width:432px">Session 2:<span class="write"></span></div>
  <div class="session" style="left:28px;top:213px;width:432px">Session 3:<span class="write"></span></div>
  <div class="note" style="left:36px;top:245px">Please give 24 hours notice cancelling your appointment or a fee may be charged</div>
</section>

</body>
</html>
```